Card Design Project

Gift Card and Gift Card Carrier Design for Spanish Tapas Restaurant/Bar

all of our current logos are on this link:
www.quint-oh-laros.com/logos.html

you can see the different files, simply click on them to download what you need

the current name of our restaurant is: Quint-oh-laro's Tapas Bar
we are moving to a new location and we are changing the spelling of our name to:
Carmoleta Tapas Bar

the font that our name is written in is: Mistral

in regards to the tone of the artwork, the look, the feel:
we are Spain Europe Tapas Cuisine.
Our restaurant has two ambiances
one ambiance is a rustic spanish feel on the first floor.
the second ambiance is a trendy ibiza moorish spanish feel.
go to this link for design elements of our new location
http://www.quint-oh-laros.com/DesignConcepts.html
this is our facebook page:
http://www.facebook.com/quintohlaros

Must provide your actual design files with layers (including all font);
Adobe AI CS4 or lower or
Adobe Photoshop CS4 file or lower

Target Market(s)

ages 25 to 45 is our biggest demographic of customer

Industry/Entity Type

Restaurant

Requirements
Must have
• the front of the gift card is the actual design
the back of the gift card must be the disclaimers for the card

here are the disclaimers:

Additional value may be added to this card at any time.
We are not reponsible for lost, stolen, or damaged cards or any unauthorized card use.
Cards that are lost, stolen, or damaged cannot be replaced and have no value.
Cards cannot be redeemed for cash and cannot be used toward tax and tips.
Card expires 180 calendar days after issue date.

Carmoleta Tapas Bar
2914 West Pellman Avenue, Chicago IL 60618

i attached samples of the backs of other cards so you can see some samples

Hints to submit a winning design:

In regards to the Logo that we provided you, you will notice the word Carmoleta.
Feel free to not have the word Carmoleta on the front of your gift card inside the logo.
You can remove the layer and only use the logo of the flamenco dancer herself.
If you feel the word Carmoleta goes with your design then keep it.
That logo has become a brand for this restaurant and people know the brand by simply looking at the flamenco lady - so it could be used with the name Carmoleta or without the name Carmoleta.
Feel free to use patterned backgrounds on the front of the card rather than solids
Also, use a different font other than mistral for any other words that you use.
If you use the words Gift Card - use another font for that. If you decide to put the wording: Tapas Bar in your design, or Tapas - use another font, do not use mistral for that wording.

in regards to colors, this restaurant has two ambiances, one is a earthy rustic spanish and another is a loungey darker trendy elegant ambiance, - if you submit really super bright colors all over your card, the super bright features of the card is a bit contradictory to the style of the restaurant.

stay with subtle color shifts and simplicity is the key.

I am going to add a photo of the food delivery bag of the restaurant.
Their food delivery bag is a matte black color bag with a red foil stamp of the flamenco lady logo - it is simple , to the point, and everyone loves the bag when they receive it with their deliveries.

They are also considering to purchase matte black gift cards because they want to do a foil stamped gift card also - so if you use a black background in your design - that can be advantageous to winning the first choice here.

```html
<!DOCTYPE html>
<html lang="en">
<head>
<meta charset="utf-8">
<title>Carmoleta Tapas Bar – Gift Card</title>
<link rel="stylesheet" href="https://fonts.googleapis.com/css2?family=Source+Sans+3:wght@400;600;700&family=Kaushan+Script&display=swap">
<style>
  :root {
    --page: #ece8e2;
    --card-black: #231f20;
    --card-white: #ffffff;
    --gold: #f2a23a;
    --gold-line: #e0a64a;
    --ink: #231f20;
    --edge: #3a3333;
    --photo-dark: #3b1f17;
    --photo-warm: #7a3a22;
    --photo-red: #9a3a2a;
  }
  * { box-sizing: border-box; margin: 0; padding: 0; }
  html, body {
    width: 1082px; height: 1200px; overflow: hidden;
    background: var(--page);
    font-family: "Source Sans 3", "Myriad Pro", Arial, sans-serif;
  }
  .canvas { position: relative; width: 1082px; height: 1200px; }

  .card {
    position: absolute;
    height: 425px;
    border: 1.5px solid var(--edge);
    background: var(--card-white);
    overflow: hidden;
  }

  /* Front */
  .card-front { left: 194px; top: 144px; width: 648px; }
  .front-brand-panel {
    position: absolute; left: 0; top: 0; width: 267px; height: 100%;
    background: var(--card-black);
  }
  .front-divider {
    position: absolute; left: 270px; top: 0; width: 3px; height: 100%;
    background: var(--gold-line);
  }
  .dancer-art {
    position: absolute; left: 40px; top: 76px; width: 170px; height: 230px;
    border-radius: 50% 50% 40% 40% / 30% 30% 60% 60%;
    background: radial-gradient(ellipse at 50% 45%, rgba(242,162,58,0.28), rgba(242,162,58,0.06) 70%, transparent 72%);
  }
  .brand-name {
    position: absolute; color: var(--gold); font-weight: 600;
    line-height: 1.05; white-space: nowrap;
  }
  .front-brand-name { left: 32px; top: 200px; font-size: 22px; }
  .front-url {
    position: absolute; left: 0; width: 267px; top: 382px;
    text-align: center; color: var(--gold); font-size: 16px;
  }
  .gift-card-title {
    position: absolute; left: 321px; top: 22px;
    font-family: "Kaushan Script", cursive; font-weight: 400;
    font-size: 62px; color: var(--gold);
    text-shadow: 2px 2px 0 var(--ink);
    letter-spacing: 1px; white-space: nowrap;
  }
  .venue-photo { position: absolute; border: 1.5px solid var(--ink); }
  .photo-lounge { left: 293px; top: 142px; width: 161px; height: 128px;
    background: linear-gradient(160deg, var(--photo-dark), var(--photo-warm) 60%, #2a1712); }
  .photo-mirror { left: 465px; top: 181px; width: 114px; height: 89px;
    background: linear-gradient(180deg, #2a1a14, var(--photo-warm) 55%, #1e120e); }
  .photo-dining { left: 338px; top: 280px; width: 114px; height: 90px;
    background: linear-gradient(135deg, var(--photo-red), #5a2318 70%, #2e1812); }
  .photo-bar { left: 466px; top: 280px; width: 157px; height: 126px;
    background: linear-gradient(180deg, #4a2418, #8a3a28 50%, #3a1c12); }

  /* Back */
  .card-back { left: 213px; top: 619px; width: 647px; }
  .back-dancer-art {
    position: absolute; left: 30px; top: 28px; width: 150px; height: 200px;
    border-radius: 50% 50% 40% 40% / 30% 30% 60% 60%;
    background: radial-gradient(ellipse at 50% 45%, rgba(242,162,58,0.22), rgba(242,162,58,0.05) 70%, transparent 72%);
  }
  .back-brand-name { left: 42px; top: 136px; font-size: 19px; }
  .back-address {
    position: absolute; left: 33px; top: 245px; font-style: normal;
    font-size: 16px; line-height: 21px; color: var(--ink);
  }
  .back-address strong { font-weight: 700; }
  .terms {
    position: absolute; left: 240px; top: 32px; width: 385px;
    color: var(--ink); white-space: nowrap;
  }
  .terms-heading {
    text-align: center; font-weight: 700; font-size: 18px; line-height: 23px;
    letter-spacing: 0.4px; margin-bottom: 22px;
  }
  .terms-list { list-style: none; font-size: 15px; line-height: 20px; }
  .terms-list li { position: relative; padding-left: 12px; margin-bottom: 16px; }
  .terms-list li::before { content: "•"; position: absolute; left: 0; }
  .mag-stripe {
    position: absolute; left: 0; top: 328px; width: 100%; height: 55px;
    background: var(--card-black);
  }
</style>
</head>
<body>
<main class="canvas">

  <section class="card card-front">
    <div class="front-brand-panel">
      <div class="dancer-art" role="img" aria-label="Line drawing of a flamenco dancer in gold"></div>
      <div class="brand-name front-brand-name">Carmoleta<br>Tapas Bar</div>
      <div class="front-url">www.quint-oh-laros.com</div>
    </div>
    <div class="front-divider"></div>
    <h1 class="gift-card-title">Gift Card</h1>
    <div class="venue-photo photo-lounge" role="img" aria-label="Photo of the dim lounge seating area"></div>
    <div class="venue-photo photo-mirror" role="img" aria-label="Photo of a mirrored wall with warm lamps"></div>
    <div class="venue-photo photo-dining" role="img" aria-label="Photo of the red-walled dining room"></div>
    <div class="venue-photo photo-bar" role="img" aria-label="Photo of the bar counter with hanging lights"></div>
  </section>

  <section class="card card-back">
    <div class="back-dancer-art" role="img" aria-label="Line drawing of a flamenco dancer in gold"></div>
    <div class="brand-name back-brand-name">Carmoleta</div>
    <address class="back-address">
      <strong>Carmoleta Tapas Bar</strong><br>
      2914 West Pellman Ave.<br>
      Chicago IL 60618
    </address>
    <div class="terms">
      <p class="terms-heading">Additional value may be added to this<br>card at any time.</p>
      <ul class="terms-list">
        <li>We are not reponsible for lost, stolen, or<br>damaged cards or any unauthorized card use.</li>
        <li>Cards that are lost, stolen, or damaged cannot<br>be replaced and have no value.</li>
        <li>Cards cannot be redeemed for cash and cannot<br>be used toward tax and tips</li>
        <li>Card expires 180 calendar days after issue date.</li>
      </ul>
    </div>
    <div class="mag-stripe"></div>
  </section>

</main>
</body>
</html>
```